Public Relations Agency Seeks Wordpress Design and Coding

TORVEX Media is a public relations agency specializing in media relations, public affairs and marketing communication.

The site should display the following visual characteristics: professionalism, trustworthiness, high-tech focus, clear and concise design.

The desired colors are royal blue, gray and hints of red.

Design look/feel inspired by this site: http://brisklanefetes.example/

Specifications:

1. Navigation/Pages/Index:

HOME

ABOUT US

SERVICES

NEWS

CONTACT

---

2. Functionality of/content for each page:

- Home
o Dominant photo (professional, edgy, innovative)
o Simple, straightforward access to/from “Home” from other pages
o Includes logo (attached) and tagline "Unleash the power of communication"
o Direct link to “CONTACT”
o Links to social media accounts: Facebook, Twitter, LinkedIn

- About Us

o Company profile blurb
o President’s photo with short bio

- Services
o Public Relations
 Strategic communication
 Brand and reputation management
 Community relations
o Media Relations
 News coverage and contacts
 Media training and interview skills
 Crisis communications
o Congressional Affairs
 Public affairs
 Public policy
 Legislative strategy
o Mass Communication
 Speechwriting
 Presentation creation
 Social media
o Marketing Communications
 Business collateral material
 Promotional campaigns
 Special events and tradeshows

- News
o Blog-like page to post information and/or share news from other sites

- Contact
o Standard “Contact Us” form (Name, Email, Phone, Message)
o Direct Contact
 (555) 314-2690
 Marlow@TORVEXmedia.example

Target Market(s)

Small to large businesses specializing in high technology, defense/military, medicine/healthcare, and wide array of professional services.

Industry/Entity Type

Marketing

Font styles to use
Serif
Sans Serif

Colors
0555a3
ec2027
edf3f7

Requirements
Must have
• -- Project reqires DESIGN - and - fully CODED.

-- Strong SEO

-- Optimized for mobile viewing

Thank you!

```html
<!DOCTYPE html>
<html lang="en">
<head>
<meta charset="utf-8">
<title>TORVEX Media</title>
<link href="https://fonts.googleapis.com/css2?family=Open+Sans:wght@600;800&family=Raleway:wght@300;400;500&display=swap" rel="stylesheet">
<style>
  :root {
    --royal-blue: #0555a3;
    --accent-red: #d9413b;
    --ink: #2b2b2b;
    --muted: #6b6b6b;
    --card-bg: #f5f8fa;
    --card-border: #e8edf1;
    --rule: #e3e6e9;
    --white: #ffffff;
    --header-tint: rgba(95, 98, 98, 0.82);
  }
  * { margin: 0; padding: 0; box-sizing: border-box; }
  html, body { width: 1200px; height: 871px; overflow: hidden; background: var(--white); }
  body { position: relative; font-family: 'Raleway', sans-serif; color: var(--ink); }

  .hero {
    position: absolute; left: 0; top: 0; width: 1200px; height: 600px;
    background:
      radial-gradient(ellipse 260px 380px at 600px 170px, rgba(225,230,228,0.85), rgba(225,230,228,0) 70%),
      linear-gradient(90deg, #2c3a2c 0%, #4d5e4b 20%, #7b8a7a 45%, #8e9b8d 55%, #566853 80%, #2f3d2f 100%);
  }
  .hero-floor {
    position: absolute; left: 0; bottom: 0; width: 1200px; height: 140px;
    background: linear-gradient(180deg, rgba(40,60,38,0) 0%, rgba(40,60,38,0.75) 100%);
  }

  .site-header {
    position: absolute; left: 0; top: 0; width: 1200px; height: 61px;
    background: var(--header-tint);
  }
  .brand {
    position: absolute; left: 148px; top: 0; width: 194px; height: 61px;
    background: var(--royal-blue);
    display: flex; align-items: center; justify-content: center;
    color: var(--white); font-family: 'Raleway', sans-serif; font-weight: 500;
    font-size: 22px; letter-spacing: 1px;
  }
  .main-nav { position: absolute; top: 0; left: 0; height: 61px; }
  .main-nav a {
    position: absolute; top: 17px; white-space: nowrap;
    color: var(--white); text-decoration: none;
    font-family: 'Raleway', sans-serif; font-weight: 300; font-size: 23px; line-height: 28px;
  }

  .tagline {
    position: absolute; left: 158px; top: 290px;
    color: var(--white); font-family: 'Open Sans', sans-serif; font-weight: 600;
    font-size: 36px; line-height: 44px;
  }
  .tagline strong { font-weight: 800; }

  .slide-arrow { position: absolute; top: 320px; width: 14px; height: 24px; }

  .social-tabs { position: absolute; left: 1165px; top: 280px; width: 35px; }
  .social-tabs a {
    display: block; width: 35px; height: 29px; margin-bottom: 2px;
    background: var(--accent-red);
  }

  .promo-title {
    position: absolute; left: 158px; top: 645px;
    font-family: 'Raleway', sans-serif; font-weight: 400; font-size: 27px; line-height: 33px; color: var(--ink);
  }
  .promo-title span { color: var(--royal-blue); }
  .promo-text {
    position: absolute; left: 158px; top: 680px; white-space: nowrap;
    font-size: 13.5px; line-height: 16px; color: var(--muted);
  }
  .promo-button {
    position: absolute; left: 909px; top: 653px; width: 134px; height: 38px;
    background: var(--accent-red);
  }
  .section-rule {
    position: absolute; left: 158px; top: 729px; width: 885px; height: 1px; background: var(--rule);
  }

  .feature-card {
    position: absolute; top: 790px; width: 285px; height: 90px;
    background: var(--card-bg); border: 1px solid var(--card-border);
    text-align: center; padding-top: 46px;
    font-family: 'Raleway', sans-serif; font-weight: 500; font-size: 17px; color: var(--ink);
  }
</style>
</head>
<body>
  <section class="hero" role="img" aria-label="Photograph of a tall misty evergreen forest seen from below">
    <div class="hero-floor"></div>
  </section>

  <header class="site-header">
    <div class="brand">TORVEX Media</div>
    <nav class="main-nav">
      <a href="#" style="left:519px">Home</a>
      <a href="#" style="left:616px">About Us</a>
      <a href="#" style="left:746px">Services</a>
      <a href="#" style="left:870px">News</a>
      <a href="#" style="left:956px">Contact</a>
    </nav>
  </header>

  <h1 class="tagline">Unleash the power<br>of <strong>communication</strong></h1>

  <svg class="slide-arrow" style="left:96px" viewBox="0 0 14 24" aria-label="Previous slide">
    <polyline points="12,2 2,12 12,22" fill="none" stroke="#ffffff" stroke-width="2"/>
  </svg>
  <svg class="slide-arrow" style="left:1141px" viewBox="0 0 14 24" aria-label="Next slide">
    <polyline points="2,2 12,12 2,22" fill="none" stroke="#ffffff" stroke-width="2"/>
  </svg>

  <div class="social-tabs">
    <a href="#" aria-label="Social profile one"></a>
    <a href="#" aria-label="Social profile two"></a>
    <a href="#" aria-label="Social profile three"></a>
  </div>

  <h2 class="promo-title">Hear more about our <span>new promotion</span></h2>
  <p class="promo-text">We care not only to create quality themes, but as well make sure users succeed to setup, easy to use admin interface.</p>
  <a class="promo-button" href="#" aria-label="Learn more"></a>
  <div class="section-rule"></div>

  <div class="feature-card" style="left:158px">Responsive Ready</div>
  <div class="feature-card" style="left:458px">Powerful Admin</div>
  <div class="feature-card" style="left:758px">Deeply Customizable</div>
</body>
</html>
```